Business Card Design Project

Hi
I'm currently getting a logo designed which will go on the front. It is designed for s
Fitness instructor/ personal training business.
On the back I would like written:
Boxing for Fitness
Aqua Fitness Professional
PersonalisedTraining 1/1 or Small Group outdoor training
Fun and unique workouts
Weight loss/ Strength training

Also I need on there my details
minawebb27@quellmail.net
0438 917 355
FB Mina Fitness

Reason: I would like to extend the deadline to give extra days after I have confirmed the logo in two days

Target Market(s)

Mostly women aged between 20-50

Industry/Entity Type

Training

Font styles to use
Sans Serif

Requirements
Must have
• My logo ( I have attached my favourite logo options )
My details

```html
<!DOCTYPE html>
<html lang="en">
<head>
<meta charset="UTF-8">
<title>Mina Fitness – Business Card</title>
<link rel="stylesheet" href="https://fonts.googleapis.com/css2?family=Arimo:wght@400&display=swap">
<style>
  :root {
    --card-white: #ffffff;
    --accent-pink: #d574ae;
    --logo-pink: #f07aa9;
    --stripe-blue: #1f5c9a;
    --ink: #1e1e1e;
    --logo-grey: #666769;
  }
  * { margin: 0; padding: 0; box-sizing: border-box; }
  html, body {
    width: 1200px;
    height: 341px;
    overflow: hidden;
    background: var(--card-white);
  }
  .card-spread {
    position: relative;
    width: 1200px;
    height: 341px;
    font-family: "Arimo", Arial, sans-serif;
    color: var(--ink);
  }
  .card-shapes {
    position: absolute;
    inset: 0;
  }
  .brand-name {
    position: absolute;
    left: 340px;
    top: 112px;
    font-size: 36px;
    font-weight: 400;
    color: var(--logo-grey);
    white-space: nowrap;
  }
  .services {
    position: absolute;
    left: 622px;
    top: 29px;
    list-style: none;
  }
  .services li {
    position: relative;
    padding-left: 25px;
    font-size: 19px;
    line-height: 35px;
    white-space: nowrap;
  }
  .services li::before {
    content: "";
    position: absolute;
    left: 1px;
    top: 11px;
    width: 14px;
    height: 14px;
    border-radius: 50%;
    background: var(--accent-pink);
  }
  .contact {
    position: absolute;
    top: 261px;
    font-size: 20px;
    line-height: 25px;
    white-space: nowrap;
  }
  .contact-front { left: 8px; }
  .contact-back { right: 8px; text-align: right; }
</style>
</head>
<body>
<main class="card-spread">
  <svg class="card-shapes" width="1200" height="341" viewBox="0 0 1200 341" aria-hidden="true">
    <path d="M0,17 C40,190 300,285 597,292 L597,341 L0,341 Z" fill="var(--accent-pink)"/>
    <path d="M1200,17 C1160,190 900,285 601,292 L601,341 L1200,341 Z" fill="var(--accent-pink)"/>
    <rect x="0" y="11" width="595" height="5" fill="var(--stripe-blue)"/>
    <rect x="601" y="11" width="599" height="5" fill="var(--stripe-blue)"/>
    <rect x="282" y="297" width="313" height="5" fill="var(--stripe-blue)"/>
    <rect x="601" y="297" width="314" height="5" fill="var(--stripe-blue)"/>
    <rect x="0" y="311" width="595" height="5" fill="var(--stripe-blue)"/>
    <rect x="601" y="311" width="599" height="5" fill="var(--stripe-blue)"/>
    <rect x="0" y="325" width="595" height="5" fill="var(--stripe-blue)"/>
    <rect x="601" y="325" width="599" height="5" fill="var(--stripe-blue)"/>
    <rect x="595" y="0" width="6" height="341" fill="var(--card-white)"/>
    <circle cx="270" cy="132" r="64" fill="var(--logo-pink)"/>
  </svg>

  <div class="brand-name">Mina Fitness</div>

  <ul class="services">
    <li>Boxing for Fitness</li>
    <li>Aqua Fitness Professional</li>
    <li>PersonalisedTraining 1/1 or Small Group outdoor training</li>
    <li>Fun and unique workouts</li>
    <li>Weight loss/ Strength training</li>
  </ul>

  <div class="contact contact-front">
    <p>0438 917 355</p>
    <p>minawebb27@quellmail.net</p>
  </div>
  <div class="contact contact-back">
    <p>0438 917 355</p>
    <p>minawebb27@quellmail.net</p>
  </div>
</main>
</body>
</html>
```